Web site for Copper Lantern Cleaner and Protectant

We need a website for a new company called Copper Lantern, LLC. We make and resell a simple spray and wipe waterless all purpose cleaner a protectant safe on all surfaces for use on RVs, boats, cars and motorcycles. This is an eco-friendly green product.

The website will be our store front with product info, training videos, events, social media feeds, and link to our markets space for purchases. We will be working to establish distributers and resellers and as such will be traveling to RV and car shows heavily the first couple of years.

It cleans and protects in a simple spray and wipe step leaving the surface protected and conditioned to repel dust, dirt, water, smudges, bugs and fingerprints while preventing fogging. Safe on acrylic, clarivex, durimon, plastic, rubber, painted surfaces, chrome, stainless, aluminum, vinyl, leather, glass.... This is an eco-friendly green product.

We want to play off the company name to tell the consumer that the product is easy to use and associate to the nostalgics 1950's in the USA.

Attached is our Logo and draft of the labels we will be using for the products. Please let me know what other information you need to get started.

Thank you

```html
<!DOCTYPE html>
<html lang="en">
<head>
<meta charset="utf-8">
<title>Copper Lantern Cleaner</title>
<link href="https://fonts.googleapis.com/css2?family=Lobster&family=Ultra&family=Limelight&display=swap" rel="stylesheet">
<style>
  :root{
    --bg:#e3e3e1;
    --blue:#4f72b8;
    --blue-dark:#3f5f9f;
    --green:#69a550;
    --green-dark:#4f8a3a;
    --cream:#f2ecd4;
    --ink:#2a2a2a;
    --text:#4a4a4a;
  }
  *{box-sizing:border-box;margin:0;padding:0}
  html,body{width:1200px;height:1200px;overflow:hidden}
  body{background:radial-gradient(ellipse at 50% 40%,#ececea 0%,var(--bg) 70%,#d9d9d7 100%);position:relative;font-family:Arial,Helvetica,sans-serif}
  .abs{position:absolute}

  /* navigation band */
  .nav-line{position:absolute;left:0;width:1200px;background:var(--green)}
  .nav-line.top{top:70px;height:5px}
  .nav-line.bottom{top:119px;height:6px}
  .nav-band{position:absolute;left:0;top:78px;width:1200px;height:39px;background:var(--blue);border-top:1px solid #c8d4ee;border-bottom:1px solid #c8d4ee}
  .nav-link{position:absolute;top:84px;transform:translateX(-50%);font-family:'Lobster',cursive;font-size:19px;color:var(--cream);text-decoration:none;text-shadow:1px 1px 0 #27406f}
  .brand{position:absolute;left:600px;top:76px;transform:translateX(-50%);display:flex;align-items:center;gap:8px;background:var(--blue);padding:0 14px;height:42px}
  .brand-dot{width:14px;height:14px;border-radius:50%;background:var(--green)}
  .brand-name{font-family:'Lobster',cursive;font-size:27px;color:var(--cream);white-space:nowrap}

  /* hero */
  .hero-panel{position:absolute;left:0;top:0}
  .hero-photo{position:absolute;left:196px;top:360px;width:410px;height:256px;border-radius:70px 40px 30px 60px;background:radial-gradient(ellipse at 55% 55%,#3b3b3f 0%,#1d1d20 55%,rgba(30,30,32,.0) 78%)}
  .eco-badge{position:absolute;left:248px;top:251px;width:92px;height:92px;border-radius:50%;background:var(--green);border:2px solid #cfe3c5}
  .eco-text{position:absolute;left:279px;top:271px;font-family:'Ultra',serif;font-size:19px;line-height:23px;color:var(--cream);text-shadow:1px 1px 0 #27406f}
  .hero-title{position:absolute;text-align:center;color:var(--cream);text-shadow:2px 3px 0 #2c2c2c}
  .hero-title.small{left:632px;top:244px;width:200px;font-family:'Ultra',serif;font-size:31px}
  .hero-title.big{font-family:'Lobster',cursive;line-height:1}
  .hero-title.line1{left:520px;top:290px;width:400px;font-size:76px}
  .hero-title.line2{left:544px;top:372px;width:400px;font-size:82px}
  .order-btn{position:absolute;left:669px;top:478px;width:137px;height:36px;background:var(--green);clip-path:polygon(0 0,100% 0,94% 50%,100% 100%,0 100%,6% 50%);font-family:'Ultra',serif;font-size:16px;color:var(--cream);text-align:center;line-height:36px;text-shadow:1px 1px 0 #2f5a22}
  .slide-arrow{position:absolute;top:538px;width:29px;height:29px;border-radius:50%;background:var(--blue-dark)}
  .slide-arrow svg{display:block}

  /* welcome */
  .welcome{position:absolute;left:208px;top:643px;font-family:'Lobster',cursive;font-size:31px;white-space:nowrap}
  .welcome .lead{color:var(--blue)}
  .welcome .name{color:var(--green)}
  .welcome-rule{position:absolute;left:658px;top:664px;width:334px;height:7px;background:repeating-linear-gradient(135deg,#bdbdbb 0 1px,transparent 1px 3px)}
  .intro{position:absolute;left:211px;width:782px;font-size:12.6px;line-height:21.7px;color:var(--text)}
  .intro.first{top:692px}
  .intro.second{top:757px}

  /* categories */
  .category{position:absolute;top:842px;width:250px;height:190px;border:6px solid var(--green);border-radius:6px;overflow:hidden;box-shadow:0 2px 4px rgba(0,0,0,.25)}
  .category .photo{position:absolute;inset:0}
  .category .label{position:absolute;left:0;right:0;bottom:8px;text-align:center;font-family:'Limelight',serif;font-size:28px;color:#fff;text-shadow:1px 1px 2px #000}
  .cat-boats{left:208px}
  .cat-boats .photo{background:linear-gradient(180deg,#e9e9e9 0%,#bfbfbf 45%,#7a7a7a 70%,#151515 100%)}
  .cat-cars{left:475px}
  .cat-cars .photo{background:linear-gradient(180deg,#d6d3cf 0%,#9a958f 40%,#3d3b38 72%,#121212 100%)}
  .cat-moto{left:742px}
  .cat-moto .photo{background:linear-gradient(160deg,#8a2f34 0%,#5b4a4c 40%,#3a3f4a 65%,#141414 100%)}

  /* footer */
  .footer-line{position:absolute;left:0;top:1062px;width:1200px;height:6px;background:var(--green)}
  .footer{position:absolute;left:0;top:1070px;width:1200px;height:130px;background:var(--blue);border-top:1px solid #c8d4ee}
  .contact-title{position:absolute;left:210px;top:1088px;font-family:'Lobster',cursive;font-size:15px;color:var(--cream)}
  .contact-phone{position:absolute;left:210px;top:1108px;font-family:'Lobster',cursive;font-size:22px;color:var(--cream)}
  .social{position:absolute;top:1148px;width:32px;height:32px;border-radius:5px;background:var(--green);border:2px solid var(--cream)}
  .footer-title{position:absolute;left:394px;top:1090px;width:400px;text-align:center;font-family:'Ultra',serif;font-size:20px;color:var(--cream);text-shadow:1px 1px 0 #27406f}
  .footer-links{position:absolute;left:394px;top:1131px;width:400px;text-align:center;font-size:12px;color:var(--cream)}
  .footer-links a{color:var(--cream);text-decoration:none}
  .footer-links .sep{margin:0 9px}
  .copyright{position:absolute;left:394px;top:1153px;width:400px;text-align:center;font-size:12px;color:var(--cream)}
  .signup-title{position:absolute;left:790px;top:1088px;width:230px;text-align:center;font-family:'Lobster',cursive;font-size:15px;color:var(--cream)}
  .signup-input{position:absolute;left:804px;top:1117px;width:190px;height:20px;border-radius:10px;background:#fff;border:2px solid var(--green);font-size:10px;font-weight:bold;color:#333;text-align:center;line-height:16px}
  .signup-btn{position:absolute;left:811px;top:1148px;width:177px;height:29px;background:var(--green);border:2px solid var(--cream);font-family:'Lobster',cursive;font-size:17px;color:var(--cream);text-align:center;line-height:25px}
</style>
</head>
<body>

<header>
  <div class="nav-line top"></div>
  <nav class="nav-band"></nav>
  <div class="nav-line bottom"></div>
  <a class="nav-link" href="#" style="left:228px">Home</a>
  <a class="nav-link" href="#" style="left:332px">About</a>
  <a class="nav-link" href="#" style="left:446px">Product</a>
  <a class="nav-link" href="#" style="left:749px">Service</a>
  <a class="nav-link" href="#" style="left:854px">Blog</a>
  <a class="nav-link" href="#" style="left:962px">Contact</a>
  <div class="brand"><span class="brand-dot"></span><span class="brand-name">Copper Lantern</span></div>
</header>

<section class="hero">
  <svg class="hero-panel" width="1200" height="640" viewBox="0 0 1200 640">
    <path d="M214 244 L980 160 Q992 158 989 172 L906 590 Q903 602 890 601 L242 581 Q232 581 231 570 L210 256 Q209 245 214 244 Z"
          fill="#4f72b8" stroke="#69a550" stroke-width="7" stroke-linejoin="round"/>
  </svg>
  <div class="hero-photo" role="img" aria-label="Photo of a black vintage 1930s sedan"></div>
  <div class="eco-badge"></div>
  <p class="eco-text">Eco-friendly<br>Green product.</p>
  <p class="hero-title small">Copper</p>
  <p class="hero-title big line1">Lantern</p>
  <p class="hero-title big line2">Cleaner</p>
  <a class="order-btn" href="#">Order Now</a>
  <span class="slide-arrow" style="left:805px"><svg width="29" height="29" viewBox="0 0 29 29"><path d="M17 8 L11 14.5 L17 21" fill="none" stroke="#6a88c6" stroke-width="2.5"/></svg></span>
  <span class="slide-arrow" style="left:840px"><svg width="29" height="29" viewBox="0 0 29 29"><path d="M12 8 L18 14.5 L12 21" fill="none" stroke="#6a88c6" stroke-width="2.5"/></svg></span>
</section>

<main>
  <h1 class="welcome"><span class="lead">Welcome to</span> <span class="name">Copper Lantern Cleaner</span></h1>
  <div class="welcome-rule"></div>
  <p class="intro first">We make and resell a simple spray and wipe waterless all purpose cleaner a protectant safe on all surfaces for use on RVs, boats, cars and motorcycles. This is an eco-friendly green product.</p>
  <p class="intro second">It cleans and protects in a simple spray and wipe step leaving the surface protected and conditioned to repel dust, dirt, water, smudges, bugs and fingerprints while preventing fogging. Safe on acrylic, clarivex, durimon, plastic, rubber, painted surfaces, chrome, stainless, aluminum, vinyl, leather, glass.</p>

  <a class="category cat-boats" href="#"><span class="photo" role="img" aria-label="Black and white photo of a boat at a harbour"></span><span class="label">BOATS</span></a>
  <a class="category cat-cars" href="#"><span class="photo" role="img" aria-label="Sepia photo of a classic car front"></span><span class="label">CARS</span></a>
  <a class="category cat-moto" href="#"><span class="photo" role="img" aria-label="Photo of motorcycle gauges and handlebars"></span><span class="label">MOTORCYCLES</span></a>
</main>

<footer>
  <div class="footer-line"></div>
  <div class="footer"></div>
  <p class="contact-title">Please Contact</p>
  <p class="contact-phone">0-555-010-274</p>
  <span class="social" style="left:207px"></span>
  <span class="social" style="left:247px"></span>
  <span class="social" style="left:287px"></span>
  <p class="footer-title">Copper Lantern Cleaner</p>
  <p class="footer-links"><a href="#">Home</a><span class="sep">|</span><a href="#">About Us</a><span class="sep">|</span><a href="#">Product</a><span class="sep">|</span><a href="#">Contact Us</a></p>
  <p class="copyright">©2014 Copperlanterncleaner. All Rights Reserved</p>
  <p class="signup-title">Get updates promos and discounts!</p>
  <div class="signup-input">Enter Your Email Here...</div>
  <div class="signup-btn">Subscribe Now!</div>
</footer>

</body>
</html>
```